Management Consulting firm needs business model Infographic

Meridian Kestrel is a diversity and inclusion consulting firm. We engage in strategy development, knowledge transfer, and coaching. Our primary colors are red (f02e25), black (241e20), grey (c7c8ca) and white (ffffff) that can be highlighted with (ED7F21), (158A8F) and (1ABB24).

We are looking for a graphical representation of the Meridian Kestrel business model. We describe what we do as addressing Diversity & Inclusion challenges and opportunities through Relevant Knowledge, Customized Strategies and Measurable Results. Our tagline is: D&I Models, Assessments and Tools for You!

We believe our business model has three stages or phases.
1. Diversity & Inclusion business challenges or opportunities arise such as changing demographics, lost market share, declining revenue, stalled innovation, attracting and retaining top talent, next-generation leadership development, abusive behavior in the workplace, etc.
2. These challenges or opportunities motivate an organization to re-examine the work culture their behaviors create, particularly the mindset, knowledge set and skillset of organizational executives
3. We develop models, assessments and tools that determine and leverage what the organization has been culturally and identify the strategies, action plans, and metrics it needs to address that business challenge or seize those business opportunity.
Thus a client can expect Meridian Kestrel to generate Relevant Knowledge, Customized Strategies and Measurable Results.

The designer can visit our website https://www.meridiankestrel.example/ , and read a blog post https://www.meridiankestrel.example/blog-news-cultural-diversity/leading-inclusively-how-cultural-competence-aids-performance for background.

The ideal infographic is one where a portion of it (or in totality) can be used as a Pagebook, WorkLoop and Chirply profile banner.

We have includes some sample infographics that we like.
1) The first is within a PowerPoint deck, Slide 1 is the original infographic template and slide 2 is an example of how MK business model could be added.
2) The other three are also styles we like.

Target Market(s)

Business executives

Industry/Entity Type

Management Consulting

Font styles to use
Sans Serif
Other font styles liked:
• Lato

Colors
ec1f27
000000
474747
0392cd
00a990
9bcb3b

Requirements
Must have
• We are looking for a graphical representation of the Meridian Kestrel business model. The design must the four components describing what we do: 1) An organization facing a Diversity & Inclusion challenge or opportunity. We address that challenge or opportunity through 2) Relevant Knowledge, 3) Customized Strategies and 4) Measurable Results.
• The design must include the tagline: D&I Models, Assessments and Tools for You!
• We prefer a horizontal / landscape.
Nice to have
• A nice to have is if the design (either in whole, or part) can be used on Pagebook, Chirply or WorkLoop profile banners
• Another nice to have is if the business challenges/opportunities component of the infographic includes examples such as changing demographics, lost market share, declining revenue, stalled innovation, attracting and retaining top talent, next-generation leadership development, abusive behavior in the workplace, etc.
• A nice to have is if the design (either in whole, or part) can be used on the back of a business a card
Should not have
• Silly, unprofessional or business pictures, or icons.

```html
<!DOCTYPE html>
<html lang="en">
<head>
<meta charset="utf-8">
<title>Meridian Kestrel – Embrace Changing Demographics</title>
<link rel="stylesheet" href="https://fonts.googleapis.com/css2?family=Barlow+Condensed:wght@500;600&family=Barlow+Semi+Condensed:wght@500&family=Barlow:wght@500;600&family=Bebas+Neue&display=swap">
<style>
  :root {
    --red: #ee1c4e;
    --orange: #f47b0c;
    --mint: #4ef0c1;
    --lime: #8bf20e;
    --blue: #3bb4ee;
    --green: #34e57a;
    --chartreuse: #8ee91b;
    --ink: #241e20;
    --slate: #474747;
    --white: #ffffff;
  }
  * { box-sizing: border-box; margin: 0; padding: 0; }
  html, body { width: 1200px; height: 756px; overflow: hidden; background: var(--white); }
  .canvas { position: relative; width: 1200px; height: 756px; overflow: hidden; background: var(--white); }
  .diagram { position: absolute; inset: 0; }

  .pillar { position: absolute; color: var(--white); }
  .pillar__title {
    font-family: "Barlow", sans-serif; font-weight: 500;
    font-size: 25px; letter-spacing: 0.4px; line-height: 1; margin-bottom: 6px;
  }
  .pillar__list {
    list-style: none; font-family: "Barlow Condensed", sans-serif; font-weight: 500;
    font-size: 17.5px; line-height: 22.4px; padding-left: 14px;
  }
  .pillar__list li::before { content: "· "; }
  .pillar--workplace { left: 280px; top: 98px; }
  .pillar--marketplace { left: 58px; top: 318px; }
  .pillar--marketplace .pillar__list { padding-left: 26px; }
  .pillar--community { left: 300px; top: 548px; }
  .pillar--community .pillar__list { padding-left: 0; }

  .hub-label {
    position: absolute; left: 350px; top: 348px; width: 158px;
    text-align: center; color: var(--red);
    font-family: "Barlow Semi Condensed", sans-serif; font-weight: 500;
    font-size: 21px; line-height: 21px; letter-spacing: 0.3px;
  }

  .headline {
    position: absolute; left: 585px; top: 236px;
    color: var(--red); font-family: "Bebas Neue", sans-serif;
    font-size: 90px; line-height: 70px; letter-spacing: 0.5px;
  }

  .stage {
    position: absolute; top: 408px; color: var(--white);
    font-family: "Barlow", sans-serif; font-weight: 500;
    font-size: 21px; line-height: 24px; letter-spacing: 1px;
  }
  .stage--knowledge { left: 586px; }
  .stage--strategies { left: 802px; }
  .stage--results { left: 1013px; }

  .signoff { position: absolute; left: 586px; top: 510px; font-family: "Barlow", sans-serif; }
  .signoff__firm { font-weight: 600; font-size: 26px; line-height: 30px; color: var(--ink); letter-spacing: 0.5px; }
  .signoff__tagline { font-weight: 500; font-size: 20px; line-height: 26px; color: var(--slate); margin-top: 4px; }
</style>
</head>
<body>
<main class="canvas">
  <svg class="diagram" width="1200" height="756" viewBox="0 0 1200 756" aria-hidden="true">
    <path class="neck neck--workplace" fill="var(--orange)" d="M318,222 Q342,252 340,275 L340,305 L402,305 L402,275 Q400,252 420,222 Z"/>
    <path class="neck neck--marketplace" fill="var(--mint)" d="M220,310 Q250,336 270,336 L305,336 L305,398 L270,398 Q250,398 220,400 Z"/>
    <path class="neck neck--community" fill="var(--lime)" d="M340,432 L402,432 L402,470 Q404,492 422,510 L316,510 Q338,492 340,470 Z"/>

    <circle cx="358" cy="146" r="112" fill="none" stroke="var(--orange)" stroke-width="1.5"/>
    <circle cx="358" cy="146" r="95" fill="var(--orange)"/>
    <circle cx="138" cy="353" r="112" fill="none" stroke="var(--mint)" stroke-width="1.5"/>
    <circle cx="138" cy="353" r="95" fill="var(--mint)"/>
    <circle cx="368" cy="585" r="112" fill="none" stroke="var(--lime)" stroke-width="1.5"/>
    <circle cx="368" cy="585" r="95" fill="var(--lime)"/>

    <circle cx="370" cy="369" r="74" fill="var(--white)"/>
    <path fill="none" stroke="var(--red)" stroke-width="10" d="M431.6,397.7 A68 68 0 1 1 418.1,320.9"/>
    <polygon fill="var(--red)" points="433,336 424,307 404,327"/>
    <path fill="none" stroke="var(--orange)" stroke-width="7" d="M334.8,339.4 A46 46 0 0 1 385.7,325.8"/>
    <path fill="none" stroke="var(--mint)" stroke-width="7" d="M326.8,384.7 A46 46 0 0 1 326.8,353.3"/>
    <path fill="none" stroke="var(--lime)" stroke-width="7" d="M385.7,412.2 A46 46 0 0 1 340.4,404.2"/>

    <rect x="527" y="242" width="6" height="249" fill="var(--blue)"/>
    <polygon fill="var(--chartreuse)" points="952,392 1148,392 1172,429 1148,466 952,466 976,429"/>
    <polygon fill="var(--green)" points="752,392 946,392 970,429 946,466 752,466 776,429"/>
    <polygon fill="var(--blue)" points="533,392 744,392 768,429 744,466 533,466"/>
  </svg>

  <section class="pillar pillar--workplace">
    <h2 class="pillar__title">WORKPLACE:</h2>
    <ul class="pillar__list">
      <li>Diversify Talent</li>
      <li>Increase Engagement</li>
      <li>Improve Performance</li>
    </ul>
  </section>

  <section class="pillar pillar--marketplace">
    <h2 class="pillar__title">MARKETPLACE:</h2>
    <ul class="pillar__list">
      <li>Gain Market Share</li>
      <li>Grow Revenue</li>
      <li>Improve Innovation</li>
    </ul>
  </section>

  <section class="pillar pillar--community">
    <h2 class="pillar__title">COMMUNITY:</h2>
    <ul class="pillar__list">
      <li>Foster Sustainability</li>
      <li>Establish Partnerships</li>
      <li>Generate Advocacy</li>
    </ul>
  </section>

  <p class="hub-label">CHALLENGES &amp;<br>OPPORTUNITIES</p>

  <h1 class="headline">EMBRACE CHANGING<br>DEMOGRAPHICS</h1>

  <p class="stage stage--knowledge">Relevant<br>Knowledge</p>
  <p class="stage stage--strategies">Customized<br>Strategies</p>
  <p class="stage stage--results">Measurable<br>Results</p>

  <footer class="signoff">
    <p class="signoff__firm">Meridian Kestrel</p>
    <p class="signoff__tagline">D&amp;I Models, Assessments and Tools for You!</p>
  </footer>
</main>
</body>
</html>
```